folding sales brochure

We need a brochure in the colors of orange, black and charcoal gray - our logo colors.
www.venmoretranslinks

Strong, clean - and something eye catching.

We are looking for graphic images and photos that depict international business, written translation, live simultaneous interpretation for conferences & events with people communicating. We have some photos, but are open to others.

This brochure will generalize our companies services.
This brochure will be used for B2B as well as Trade Show booths.

Reason: Project has been extended to allow time for feedback and completion. Thank you all... some wonderful designs.

Thank you all for your designs - they were all creative in so many different ways, making the choice of just one very difficult.

regards,
Harriet

Target Market(s)

Our target is large global corporate companies.

Industry/Entity Type

Events

Requirements
Must have
• company logo (will supply)
company website and address etc.

Our Type Font is: Helvetica Neue LT Std

All info needed can be found here: www.venmoretranslinks
Should not have
• we feel globes and flags are overdone in the International marketplace - hopefully you can find something else to speak Global.

```html
<!DOCTYPE html>
<html lang="en">
<head>
<meta charset="utf-8">
<title>Venmore Translinks – Folding Brochure</title>
<link rel="stylesheet" href="https://fonts.googleapis.com/css2?family=Arimo:wght@400;700&display=swap">
<style>
  :root {
    --orange: #d6762e;
    --orange-deep: #c4621f;
    --orange-light: #f08b3a;
    --orange-pale: #f6a45c;
    --charcoal: #5b5b5f;
    --charcoal-dark: #3e3e42;
    --label: #a9a9a9;
    --white: #ffffff;
    --sheet: #ffffff;
  }
  * { box-sizing: border-box; margin: 0; padding: 0; }
  html, body { width: 1200px; height: 898px; overflow: hidden; background: var(--sheet); }
  body { font-family: "Arimo", Helvetica, Arial, sans-serif; position: relative; }

  .sheet-frame { position: absolute; inset: 0; border: 1px solid #555; }

  .page-label {
    position: absolute; color: var(--label); font-size: 19px; transform: translateX(-50%);
  }
  .page-label--back { left: 326px; top: 8px; }
  .page-label--front { left: 876px; top: 10px; }
  .page-label--size { left: 632px; top: 869px; }

  .panel { position: absolute; top: 35px; height: 825px; overflow: hidden; }
  .panel--back { left: 17px; width: 583px; border: 1px solid #444; }
  .panel--front { left: 600px; width: 582px; }
  .panel-art { position: absolute; inset: 0; width: 100%; height: 100%; }

  .back-web {
    position: absolute; top: 489px; left: 0; width: 100%; padding-left: 22px;
    text-align: center; color: var(--white); font-size: 16.5px;
  }

  .brand { position: absolute; display: flex; align-items: center; }
  .brand-dot { border-radius: 50%; background: var(--orange-pale); flex: none; }
  .brand-name { color: var(--charcoal-dark); font-weight: 400; line-height: 1; }

  .brand--front { left: 44px; top: 66px; gap: 14px; }
  .brand--front .brand-dot { width: 62px; height: 62px; }
  .brand--front .brand-name { font-size: 50px; }

  .brand--back { left: 24px; top: 724px; gap: 8px; }
  .brand--back .brand-dot { width: 44px; height: 44px; }
  .brand--back .brand-name { font-size: 30px; }

  .contact {
    position: absolute; left: 194px; top: 719px; color: var(--white);
    font-size: 9.4px; line-height: 11px;
  }
  .contact-name { font-weight: 700; }
  .contact-gap { margin-top: 4px; }

  .headline {
    position: absolute; left: 234px; top: 660px; color: var(--white);
    font-size: 34px; line-height: 42px; font-weight: 400; letter-spacing: 0.2px;
  }
</style>
</head>
<body>
  <div class="sheet-frame"></div>
  <span class="page-label page-label--back">Back</span>
  <span class="page-label page-label--front">front</span>

  <!-- Back panel -->
  <section class="panel panel--back">
    <svg class="panel-art" viewBox="0 0 583 825" preserveAspectRatio="none">
      <defs>
        <linearGradient id="backBg" x1="0" y1="0" x2="1" y2="1">
          <stop offset="0" stop-color="#d0702a"/>
          <stop offset="0.6" stop-color="#d6772f"/>
          <stop offset="1" stop-color="#cc6a25"/>
        </linearGradient>
      </defs>
      <rect width="583" height="825" fill="url(#backBg)"/>
      <g fill="var(--orange-light)" opacity="0.55">
        <rect x="300" y="548" width="283" height="26"/>
        <rect x="330" y="585" width="253" height="24"/>
        <rect x="150" y="618" width="433" height="22"/>
        <rect x="270" y="650" width="313" height="30"/>
        <rect x="0" y="560" width="250" height="10" opacity="0.5"/>
      </g>
      <g fill="var(--orange-pale)" opacity="0.4">
        <rect x="230" y="596" width="240" height="3"/>
        <rect x="380" y="668" width="203" height="3"/>
        <rect x="0" y="545" width="583" height="3"/>
      </g>
      <rect x="0" y="517" width="583" height="6" fill="var(--orange-pale)"/>
      <rect x="0" y="527" width="583" height="15" fill="var(--charcoal)"/>
    </svg>
    <p class="back-web">www.venmoretranslinks.com</p>
    <div class="brand brand--back">
      <span class="brand-dot"></span>
      <span class="brand-name">Venmore</span>
    </div>
    <address class="contact" style="font-style:normal">
      <div class="contact-name">Venmore Translinks</div>
      <div>4127 Harbourline Avenue, Suite 210 Marlow, CA 90412</div>
      <div>Mailing address: P.O. Box 552109 Marlow, CA 90419</div>
      <div class="contact-gap">Phone:+1 555 214 0387 | Toll free:+1 800 555 0142</div>
      <div>Fax:+1 555 214 0390 | Email: info@venmoretranslinks.com</div>
    </address>
  </section>

  <!-- Front panel -->
  <section class="panel panel--front">
    <svg class="panel-art" viewBox="0 0 582 825" preserveAspectRatio="none">
      <defs>
        <linearGradient id="frontBg" x1="0" y1="0" x2="1" y2="1">
          <stop offset="0" stop-color="#d4722b"/>
          <stop offset="0.5" stop-color="#d97a31"/>
          <stop offset="1" stop-color="#c96823"/>
        </linearGradient>
        <linearGradient id="photoTone" x1="0" y1="0" x2="1" y2="1">
          <stop offset="0" stop-color="#f0a35e"/>
          <stop offset="0.55" stop-color="#d27834"/>
          <stop offset="1" stop-color="#8a4418"/>
        </linearGradient>
      </defs>
      <rect width="582" height="825" fill="url(#frontBg)"/>
      <g fill="var(--orange-light)" opacity="0.55">
        <rect x="320" y="155" width="262" height="30"/>
        <rect x="400" y="192" width="182" height="22"/>
        <rect x="240" y="553" width="342" height="20"/>
        <rect x="330" y="582" width="252" height="28"/>
        <rect x="120" y="620" width="462" height="22"/>
      </g>
      <g fill="var(--orange-pale)" opacity="0.45">
        <rect x="300" y="222" width="282" height="3"/>
        <rect x="250" y="598" width="332" height="3"/>
      </g>
      <polygon points="240,241 582,241 582,519 16,519" fill="url(#photoTone)"
               role="img" aria-label="Photo: business people communicating in an international setting"/>
      <polygon points="243,245 582,245 582,515 24,515" fill="none" stroke="var(--white)" stroke-width="2" opacity="0.85"/>
      <rect x="0" y="517" width="582" height="6" fill="var(--orange-pale)"/>
      <rect x="0" y="527" width="582" height="15" fill="var(--charcoal)"/>
    </svg>
    <div class="brand brand--front">
      <span class="brand-dot"></span>
      <span class="brand-name">Venmore</span>
    </div>
    <h1 class="headline">SEAMLESS LIVE<br>MULTILINGUAL<br>COMMUNICATION</h1>
  </section>

  <span class="page-label page-label--size">Each page A4 size</span>
</body>
</html>
```